Trellmark Vista brochure

A brochure based on the word document provided. Brochure provided in Word and PDF format. Should include pictures and shorten to make it a brochure of no more than two 8.5x11 pages. Completed brochure file must be under 5 megabytes.

Leadership

• final file size less than 5 megabytes. also file in Word and PDF and any other that makes sense. Must have pictures or graphics to support the text. Include the 3 logos attached from TKR, qoVantra, and Trellmark vista. qoVantra logo is in attachments you can get logo for Trellmark Vista at www.trellmarkvista.com. or http://www.trellmarkvista.com/images/logo.png

```html
<!DOCTYPE html>
<html lang="en">
<head>
<meta charset="utf-8">
<title>Trellmark Vista brochure</title>
<link href="https://fonts.googleapis.com/css2?family=Oswald:wght@300;400&family=Roboto:wght@300&family=Roboto+Condensed:wght@300;700&display=swap" rel="stylesheet">
<style>
  :root {
    --brand-blue: #0ca2cf;
    --panel-blue: #3aa6cf;
    --logo-blue: #1d93d2;
    --accent-orange: #f07a22;
    --ink: #333333;
    --ink-strong: #111111;
    --partner-red: #a3172f;
    --paper: #ffffff;
  }
  * { box-sizing: border-box; margin: 0; padding: 0; }
  html, body { width: 1200px; height: 794px; overflow: hidden; background: var(--paper); }
  .spread { position: relative; width: 1200px; height: 794px; background: var(--paper); font-family: "Roboto Condensed", sans-serif; color: var(--ink); }
  .abs { position: absolute; }

  /* back page */
  .web-address { left: 0; width: 598px; top: 50px; text-align: center; font-family: "Oswald", sans-serif; font-weight: 300; font-size: 21px; letter-spacing: 2px; color: #444; }
  .contact-panel { left: 26px; top: 103px; width: 548px; height: 560px; background: linear-gradient(160deg, #48b0d6 0%, var(--panel-blue) 50%, #2f98c4 100%); color: #fff; font-family: "Oswald", sans-serif; font-weight: 300; text-align: center; }
  .contact-title { position: absolute; left: 0; right: 0; top: 94px; font-size: 21px; font-weight: 400; letter-spacing: 2px; }
  .contact-rule { position: absolute; left: 159px; width: 234px; top: 133px; height: 2px; background: #fff; }
  .contact-icon { position: absolute; left: 255px; width: 40px; height: 40px; }
  .contact-line { position: absolute; left: 0; right: 0; font-size: 16px; letter-spacing: 1.6px; }

  .brand-name { font-family: "Roboto Condensed", sans-serif; font-weight: 700; color: var(--logo-blue); white-space: nowrap; display: flex; align-items: center; gap: 8px; }
  .brand-dot { border-radius: 50%; background: var(--logo-blue); display: inline-block; }
  .partner-name { font-family: "Roboto Condensed", sans-serif; font-weight: 700; white-space: nowrap; display: flex; align-items: center; gap: 5px; }
  .partner-square { display: inline-block; width: 20px; height: 20px; background: var(--partner-red); }
  .partner-badge { background: var(--partner-red); }
  .partner-badge-dark { background: #4a4a4a; }

  /* cover */
  .tile { position: absolute; }
  .tile-text { background: var(--brand-blue); color: #fff; font-family: "Roboto", sans-serif; font-weight: 300; font-size: 21px; line-height: 1.22; display: flex; align-items: center; padding-left: 32px; }
  .photo { background: linear-gradient(135deg, #c9d3da, #9aa6ae); }
  .photo-boardroom { background: linear-gradient(180deg, #1c3d6b 0%, #2d6aa4 45%, #0e2440 100%); }
  .photo-team { background: linear-gradient(100deg, #d9d5cf 0%, #eceff1 55%, #f4f6f7 100%); }
  .photo-ideas-1 { background: linear-gradient(135deg, #6f7276, #c9cbcd); }
  .photo-ideas-2 { background: linear-gradient(135deg, #5d6064, #d4d6d8); }
  .photo-ideas-3 { background: linear-gradient(135deg, #c5c7ca, #eef0f2); }
  .cover-intro { left: 631px; width: 548px; top: 682px; text-align: center; font-weight: 300; font-size: 16.5px; line-height: 24.5px; color: var(--ink); }
  .cover-intro strong { font-weight: 700; color: var(--ink-strong); }
</style>
</head>
<body>
<main class="spread">

  <!-- back page -->
  <p class="abs web-address">www.trellmarkvista.com</p>

  <section class="abs contact-panel" aria-label="Contact details">
    <h2 class="contact-title">CONTACT US</h2>
    <div class="contact-rule"></div>

    <svg class="contact-icon" style="top:159px" viewBox="0 0 40 40" aria-hidden="true">
      <circle cx="20" cy="20" r="18.5" fill="none" stroke="#fff" stroke-width="2.4"/>
      <path d="M9 19c2-5 20-5 22 0l-1 3h-4l-1-3c-3-1-7-1-10 0l-1 3h-4z" fill="#fff"/>
      <path d="M13 21h14l2 7H11z" fill="#fff"/>
      <circle cx="20" cy="24.5" r="2.3" fill="#3aa6cf"/>
    </svg>
    <p class="contact-line" style="top:208px">+ 1 800-555-0142 (toll-free)</p>
    <p class="contact-line" style="top:231px">+1 555-201-0188</p>

    <svg class="contact-icon" style="top:279px" viewBox="0 0 40 40" aria-hidden="true">
      <circle cx="20" cy="20" r="18.5" fill="none" stroke="#fff" stroke-width="2.4"/>
      <rect x="14" y="10" width="11" height="8" fill="#fff"/>
      <rect x="10" y="17" width="20" height="10" rx="1.5" fill="#fff"/>
      <rect x="13" y="26" width="14" height="4" fill="#fff"/>
      <rect x="13" y="20" width="10" height="1.6" fill="#3aa6cf"/>
    </svg>
    <p class="contact-line" style="top:328px">+1 555-201-0190</p>

    <svg class="contact-icon" style="top:379px" viewBox="0 0 40 40" aria-hidden="true">
      <circle cx="20" cy="20" r="18.5" fill="none" stroke="#fff" stroke-width="2.4"/>
      <rect x="10" y="13" width="20" height="14" rx="1.5" fill="#fff"/>
      <path d="M10.5 14l9.5 7.5 9.5-7.5" fill="none" stroke="#3aa6cf" stroke-width="1.6"/>
    </svg>
    <p class="contact-line" style="top:425px">info@trellmarkvista.com</p>
  </section>

  <div class="abs brand-name" style="left:40px; top:712px; font-size:29px;">
    <span>Trellmark Vista</span><span class="brand-dot" style="width:30px;height:30px;"></span>
  </div>

  <div class="abs partner-name" style="left:320px; top:693px; font-size:14px; color:var(--partner-red);">
    <span class="partner-square"></span><span>TKR</span>
  </div>
  <div class="abs partner-name" style="left:445px; top:693px; font-size:15px; color:var(--accent-orange);">
    <span class="brand-dot" style="width:20px;height:20px;background:#29a6dd;"></span><span>qoVantra</span>
  </div>
  <div class="abs partner-badge" style="left:320px; top:739px; width:84px; height:26px;" role="img" aria-label="Norwell University partner badge"></div>
  <div class="abs partner-badge-dark" style="left:445px; top:740px; width:44px; height:26px;" role="img" aria-label="Brannock School of Business partner badge"></div>

  <!-- cover -->
  <div class="abs brand-name" style="left:635px; top:40px; font-size:38px;">
    <span>Trellmark Vista</span><span class="brand-dot" style="width:42px;height:42px;"></span>
  </div>
  <div class="abs partner-name" style="left:998px; top:48px; font-size:15px; color:var(--accent-orange);">
    <span class="brand-dot" style="width:22px;height:22px;background:#29a6dd;"></span><span>qoVantra</span>
  </div>
  <div class="abs partner-name" style="left:1087px; top:49px; font-size:14px; color:var(--partner-red);">
    <span class="partner-square"></span><span>TKR</span>
  </div>

  <div class="tile tile-text" style="left:631px; top:103px; width:178px; height:183px;">Take Charge<br>of your own<br>Learning</div>
  <div class="tile photo photo-boardroom" style="left:815px; top:103px; width:364px; height:183px;" role="img" aria-label="Silhouetted business team by city windows with a tablet showing statistics"></div>

  <div class="tile photo photo-team" style="left:631px; top:291px; width:363px; height:184px;" role="img" aria-label="Colleagues reviewing a chart on a whiteboard"></div>
  <div class="tile tile-text" style="left:999px; top:291px; width:180px; height:184px;">Excel and be<br>Excellent</div>

  <div class="tile photo photo-ideas-1" style="left:631px; top:480px; width:178px; height:183px;" role="img" aria-label="Businessman touching a glowing light bulb icon"></div>
  <div class="tile photo photo-ideas-2" style="left:815px; top:480px; width:179px; height:183px;" role="img" aria-label="Business suit with a rising line of idea icons"></div>
  <div class="tile photo photo-ideas-3" style="left:999px; top:480px; width:180px; height:183px;" role="img" aria-label="Blurred office with idea icons on a graph line"></div>

  <p class="abs cover-intro">Learn about <strong>Individual Membership</strong> and optional <strong>Manager Associate Membership</strong> in the Trellmark Vista and The Tekor Centre for Team Research, Brannock School of Business, Norwell University</p>

</main>
</body>
</html>
```